Halvorsen Partners Business Card

Halvorsen Partners Civil Construction
Marcus Halvorsen
CEO
727-518-6094
Marcus@HalvorsenSiteworks.example
www.HalvorsenSiteworks.example
Site Development
Utility Construction
Excavation
40876 County Lane 19
Land O' Lakes, FL 34638

Target Market(s)

Construction and government

Industry/Entity Type

Business

Contact Information for Business Card

I want an unique design that make a statement

Number of Pages Required

1 page

Font styles to use

Colors

Designer to choose colors to be used in the design.

Requirements
Must have
• unique design, feel free to modify or change the color of my logo.
Nice to have
• extra design features like spot UV, foil accents, color edges, unique paper, or any thing that would make my card pop.
• I like the feel of the image that I attached

```html
<!DOCTYPE html>
<html lang="en">
<head>
<meta charset="utf-8">
<title>Halvorsen Partners Business Card</title>
<link href="https://fonts.googleapis.com/css2?family=Open+Sans:wght@400;600&family=Ubuntu:wght@500;700&display=swap" rel="stylesheet">
<style>
  :root {
    --backdrop: #7a797a;
    --card-dark: #1b1b1c;
    --card-light: #f4f4f3;
    --brand-blue: #2f4fa0;
    --steel-grey: #8a8a8c;
    --ink-grey: #5a5a5c;
    --rule-grey: #9a9a9c;
  }
  * { box-sizing: border-box; margin: 0; padding: 0; }
  html, body {
    width: 1200px; height: 900px; overflow: hidden;
    background: var(--backdrop);
    font-family: "Open Sans", Arial, sans-serif;
  }
  .canvas {
    width: 1200px; height: 900px;
    display: flex; align-items: center; justify-content: center; gap: 40px;
  }
  .card {
    width: 540px; height: 309px;
    position: relative;
    box-shadow: 0 6px 18px rgba(0,0,0,.35);
  }

  /* Front: dark side */
  .card-front { background: var(--card-dark); color: var(--steel-grey); }
  .brand {
    position: absolute; left: 40px; top: 44px;
    display: flex; align-items: center; gap: 18px;
  }
  .brand-square {
    width: 54px; height: 54px; background: var(--brand-blue);
  }
  .brand-divider {
    width: 1px; height: 78px; background: #444446;
  }
  .brand-name {
    font-family: "Ubuntu", "Open Sans", sans-serif;
    font-weight: 700; font-size: 33px; letter-spacing: .5px;
    text-transform: uppercase; color: var(--brand-blue); line-height: 1;
  }
  .brand-tagline {
    font-size: 17px; letter-spacing: 6px; text-transform: uppercase;
    color: var(--steel-grey); margin-top: 6px;
  }
  .services {
    position: absolute; left: 0; right: 0; top: 168px;
    display: flex; flex-direction: column; align-items: center;
  }
  .services-rule { width: 150px; height: 2px; background: var(--rule-grey); margin-bottom: 12px; }
  .service { font-size: 15px; color: var(--steel-grey); line-height: 1.35; }
  .service-dot { width: 3px; height: 3px; border-radius: 50%; background: var(--brand-blue); margin: 2px 0; }

  /* Back: light side */
  .card-back { background: var(--card-light); color: var(--ink-grey); }
  .person { position: absolute; left: 0; right: 0; top: 56px; text-align: center; }
  .person-name {
    font-family: "Ubuntu", "Open Sans", sans-serif;
    font-weight: 700; font-size: 34px; color: var(--brand-blue); line-height: 1;
  }
  .person-title {
    font-size: 22px; letter-spacing: 10px; color: var(--steel-grey); margin-top: 4px;
  }
  .contacts {
    position: absolute; left: 0; right: 0; top: 150px;
    display: flex; flex-direction: column; align-items: center; gap: 4px;
  }
  .contact-icon { width: 20px; height: 20px; display: block; }
  .contact-text { font-size: 16px; color: var(--ink-grey); margin-bottom: 4px; }
</style>
</head>
<body>
<main class="canvas">
  <section class="card card-front">
    <div class="brand">
      <div class="brand-square"></div>
      <div class="brand-divider"></div>
      <div class="brand-words">
        <div class="brand-name">Halvorsen Partners</div>
        <div class="brand-tagline">Civil Construction</div>
      </div>
    </div>
    <div class="services">
      <div class="services-rule"></div>
      <div class="service">Site Development</div>
      <div class="service-dot"></div>
      <div class="service">Utility Construction</div>
      <div class="service-dot"></div>
      <div class="service">Excavation</div>
    </div>
  </section>

  <section class="card card-back">
    <div class="person">
      <div class="person-name">Marcus Halvorsen</div>
      <div class="person-title">CEO</div>
    </div>
    <div class="contacts">
      <svg class="contact-icon" viewBox="0 0 24 24" aria-hidden="true">
        <path d="M6.6 10.8c1.4 2.8 3.8 5.1 6.6 6.6l2.2-2.2c.3-.3.7-.4 1-.2 1.1.4 2.3.6 3.6.6.6 0 1 .4 1 1V20c0 .6-.4 1-1 1C10.6 21 3 13.4 3 4c0-.6.4-1 1-1h3.5c.6 0 1 .4 1 1 0 1.3.2 2.5.6 3.6.1.3 0 .7-.2 1z" fill="#5a5a5c"/>
      </svg>
      <div class="contact-text">727-518-6094</div>
      <svg class="contact-icon" viewBox="0 0 24 24" aria-hidden="true">
        <rect x="3" y="6" width="18" height="13" fill="none" stroke="#5a5a5c" stroke-width="1.6"/>
        <path d="M3 6l9 7 9-7" fill="none" stroke="#5a5a5c" stroke-width="1.6"/>
      </svg>
      <div class="contact-text">Marcus@HalvorsenSiteworks.example</div>
      <svg class="contact-icon" viewBox="0 0 24 24" aria-hidden="true">
        <circle cx="12" cy="12" r="9" fill="none" stroke="#5a5a5c" stroke-width="1.6"/>
        <ellipse cx="12" cy="12" rx="4" ry="9" fill="none" stroke="#5a5a5c" stroke-width="1.4"/>
        <path d="M3 12h18M4.5 7.5h15M4.5 16.5h15" stroke="#5a5a5c" stroke-width="1.2"/>
      </svg>
      <div class="contact-text">www.HalvorsenSiteworks.example</div>
    </div>
  </section>
</main>
</body>
</html>
```